Faris Methani Business Card

I would like an elegant business card design in both english and arabic.

Ideally a logo design with my name in Arabic (could be a tiger for example)

It should have my Name : Faris Methani
Title: Advisor / Investor
Tel. UAE +971 558 274 903
UK +44 7821 560 287
Email. farmethani412@mailvane.net

I am an active angle investor and have many business interests in the TMT space and invest globally, the design needs to be fresh, elegant and striking.

The design should be catching and grab one's attention when they view the card.

Front card should be in English and Reverse in Arabic....

Target Market(s)

Global Investors, CEO's

Industry/Entity Type

Business

Contact Information for Business Card

Title: Advisor / Investor
Tel. UAE +971 558 274 903
UK +44 7821 560 287

Font styles to use
Serif
Other font styles liked:
• Palantino

Requirements
Must have
• A striking design with a play of my name in Arabic, could be my name that is designed as a tiger for example

```html
<!DOCTYPE html>
<html lang="en">
<head>
<meta charset="utf-8">
<title>Faris Methani – Business Card</title>
<link rel="stylesheet" href="https://fonts.googleapis.com/css2?family=Roboto+Slab:wght@300;400&display=swap">
<style>
  :root {
    --page: #2b2b2d;
    --navy: #0d3a6a;
    --navy-deep: #0a2a4f;
    --navy-glow: #1a5aa0;
    --paper: #ffffff;
    --ink: #3a3a3a;
    --ink-soft: #5a5a5a;
    --stone: #a3a3a5;
    --accent-red: #c8262a;
    --accent-blue: #1d6fc4;
  }
  * { margin: 0; padding: 0; box-sizing: border-box; }
  html, body {
    width: 1200px; height: 1000px; overflow: hidden;
    background: var(--page);
    font-family: "Roboto Slab", Georgia, serif;
  }
  .canvas { position: relative; width: 1200px; height: 1000px; }
  .card {
    position: absolute; left: 230px; width: 740px; height: 420px;
    background: var(--paper); overflow: hidden;
    box-shadow: 0 12px 30px rgba(0,0,0,.45);
  }
  .card--front { top: 50px; }
  .card--back { top: 530px; }

  /* front */
  .front__sky { position: absolute; left: 0; top: 0; width: 100%; height: 100%; }
  .brand { position: absolute; right: 46px; top: 40px; color: var(--paper); text-align: left; }
  .brand__row { display: flex; align-items: center; gap: 12px; }
  .brand__dot { width: 20px; height: 20px; border-radius: 50%; background: var(--accent-red); }
  .brand__name { font-size: 62px; font-weight: 300; line-height: 1; }
  .brand__surname { font-size: 30px; font-weight: 400; margin-top: 6px; letter-spacing: 1px; }
  .brand__title { font-size: 17px; font-weight: 300; margin-top: 2px; letter-spacing: .5px; }

  .contact { position: absolute; display: flex; align-items: flex-start; gap: 14px; color: var(--ink); }
  .contact__icon {
    width: 30px; height: 30px; border-radius: 50%; flex: none;
    display: flex; align-items: center; justify-content: center;
  }
  .contact__icon--phone { background: var(--accent-blue); margin-top: 6px; }
  .contact__icon--mail { background: var(--accent-red); }
  .contact__text { font-size: 17px; line-height: 1.35; }
  .contact--phone { left: 62px; bottom: 40px; }
  .contact--mail { right: 46px; top: 276px; align-items: center; }
  .contact--mail .contact__text { font-size: 15px; }

  /* back */
  .back__skyline { position: absolute; left: 0; top: 0; width: 100%; height: 100%; }
  .mark { position: absolute; left: 44px; top: 116px; display: flex; align-items: center; gap: 8px; color: var(--ink); }
  .mark__name { font-size: 34px; font-weight: 300; line-height: 1; }
  .mark__dot { width: 11px; height: 11px; border-radius: 50%; background: var(--accent-red); }
  .back__blurb {
    position: absolute; left: 180px; top: 96px; width: 520px;
    font-size: 17px; line-height: 1.4; color: var(--ink-soft); font-weight: 300; text-align: center;
  }
  .back__web { position: absolute; right: 60px; bottom: 120px; font-size: 26px; color: var(--accent-red); letter-spacing: 1px; }
</style>
</head>
<body>
<main class="canvas">

  <section class="card card--front" aria-label="Business card front">
    <svg class="front__sky" viewBox="0 0 740 420" role="img" aria-label="Night-blue sky above a white city skyline silhouette">
      <defs>
        <radialGradient id="skyGlow" cx="0.45" cy="0.35" r="0.7">
          <stop offset="0" stop-color="#1a5aa0"/>
          <stop offset="0.6" stop-color="#0d3a6a"/>
          <stop offset="1" stop-color="#0a2a4f"/>
        </radialGradient>
      </defs>
      <rect x="0" y="0" width="740" height="250" fill="url(#skyGlow)"/>
    </svg>

    <div class="brand">
      <div class="brand__row">
        <span class="brand__name">Faris</span>
        <span class="brand__dot"></span>
      </div>
      <div class="brand__surname">Methani</div>
      <div class="brand__title">Advisor / Investor</div>
    </div>

    <div class="contact contact--mail">
      <span class="contact__icon contact__icon--mail">
        <svg width="16" height="12" viewBox="0 0 16 12"><rect x="0.5" y="0.5" width="15" height="11" fill="none" stroke="#fff"/><path d="M0.5 0.5 L8 7 L15.5 0.5" fill="none" stroke="#fff"/></svg>
      </span>
      <span class="contact__text">farmethani412@mailvane.net</span>
    </div>

    <div class="contact contact--phone">
      <span class="contact__icon contact__icon--phone">
        <svg width="16" height="16" viewBox="0 0 24 24"><path fill="#fff" d="M6.6 10.8a15.2 15.2 0 0 0 6.6 6.6l2.2-2.2a1 1 0 0 1 1-.25 11.4 11.4 0 0 0 3.6.57 1 1 0 0 1 1 1V20a1 1 0 0 1-1 1A17 17 0 0 1 3 4a1 1 0 0 1 1-1h3.5a1 1 0 0 1 1 1c0 1.25.2 2.45.57 3.57a1 1 0 0 1-.25 1z"/></svg>
      </span>
      <span class="contact__text">Tel. UAE +971 558 274 903<br>UK +44 7821 560 287</span>
    </div>
  </section>

  <section class="card card--back" aria-label="Business card back">
    <svg class="back__skyline" viewBox="0 0 740 420" role="img" aria-label="Grey city skyline silhouette">
      <rect x="0" y="310" width="740" height="110" fill="#a3a3a5"/>
      <rect x="360" y="195" width="380" height="115" fill="#a3a3a5"/>
    </svg>

    <div class="mark">
      <span class="mark__name">Faris</span>
      <span class="mark__dot"></span>
    </div>

    <p class="back__blurb">Lorem ipsum dolor sit amet, consectetur adipiscing elit, sed do eiusmod tempor incididunt ut labore et dolore magna aliqua. Ut enim ad minim veniam, quis nostrud exercitation ullamco laboris.</p>

    <div class="back__web">www.farmethani.com</div>
  </section>

</main>
</body>
</html>
```